Tervolan Pty Ltd professional business card

A professional business card template using the colours from the supplied logo.
Clean crisp lines while, Modern while not being over the top.

Target Market(s)

Construction, commerical and industrial

Industry/Entity Type

Communications

Contact Information for Business Card

For a Communications, IT, Optical fibre installation company

Colors
37b8a4

```html
<!DOCTYPE html>
<html lang="en">
<head>
<meta charset="UTF-8">
<title>Tervolan Pty Ltd — Business Card</title>
<link rel="stylesheet" href="https://fonts.googleapis.com/css2?family=Poppins:wght@400;500&display=swap">
<style>
  :root {
    --backdrop: #d4d4d4;
    --teal: #1f93a0;
    --white: #ffffff;
    --ink: #333333;
  }
  * { margin: 0; padding: 0; box-sizing: border-box; }
  html, body {
    width: 1200px; height: 1000px; overflow: hidden;
    background: var(--backdrop);
    font-family: "Poppins", sans-serif;
  }
  .card {
    position: absolute; left: 219px; width: 762px; height: 436px;
    overflow: hidden;
  }
  .card--front { top: 48px; background: var(--white); }
  .card--back { top: 516px; background: var(--teal); display: flex; align-items: center; justify-content: center; }
  .front-shape { position: absolute; inset: 0; width: 762px; height: 436px; }
  .wordmark { color: var(--white); font-weight: 500; letter-spacing: 1px; line-height: 1; }
  .wordmark--corner { position: absolute; right: 26px; top: 36px; font-size: 42px; }
  .wordmark--center { font-size: 80px; letter-spacing: 2px; }
  .person { position: absolute; left: 27px; top: 172px; }
  .person__name { color: var(--teal); font-size: 29px; font-weight: 400; line-height: 1.1; }
  .person__title { color: var(--ink); font-size: 16px; font-weight: 500; margin-top: 2px; }
  .contacts { position: absolute; left: 26px; top: 293px; list-style: none; }
  .contacts__item { display: flex; align-items: center; height: 31.5px; color: var(--ink); font-size: 19px; }
  .contacts__icon { width: 22px; height: 22px; margin-right: 13px; fill: none; stroke: var(--teal); stroke-width: 1.4; }
</style>
</head>
<body>
  <section class="card card--front">
    <svg class="front-shape" viewBox="0 0 762 436" aria-hidden="true">
      <rect width="762" height="436" fill="var(--teal)"/>
      <path d="M0 136 C 150 62, 520 30, 762 292 L762 436 L0 436 Z" fill="var(--white)"/>
    </svg>
    <div class="wordmark wordmark--corner">TERVOLAN</div>
    <div class="person">
      <h1 class="person__name">MARA ELLISON</h1>
      <p class="person__title">President</p>
    </div>
    <ul class="contacts">
      <li class="contacts__item">
        <svg class="contacts__icon" viewBox="0 0 24 24" aria-hidden="true"><path d="M5 3l4 1 1 5-2 1.5a11 11 0 0 0 5.5 5.5L15 14l5 1 1 4-2 2C10 21 3 14 3 5z"/><path d="M14 4a6 6 0 0 1 6 6M14 7a3 3 0 0 1 3 3"/></svg>
        (615) 555-0142
      </li>
      <li class="contacts__item">
        <svg class="contacts__icon" viewBox="0 0 24 24" aria-hidden="true"><rect x="2" y="5" width="20" height="14"/><path d="M2 5l10 8 10-8M2 19l7-7M22 19l-7-7"/></svg>
        hello@tervolan.com
      </li>
      <li class="contacts__item">
        <svg class="contacts__icon" viewBox="0 0 24 24" aria-hidden="true"><circle cx="12" cy="12" r="10"/><ellipse cx="12" cy="12" rx="4.5" ry="10"/><path d="M2 12h20M4 6.5h16M4 17.5h16M12 2v20"/></svg>
        www.tervolan.com
      </li>
    </ul>
  </section>

  <section class="card card--back">
    <div class="wordmark wordmark--center">TERVOLAN</div>
  </section>
</body>
</html>
```